Spring Anti-wrinkle Injections Poster

A1 size poster for Spring promoting anti-wrinkle injections (Velarix)
Poster is to promote rejuvination and refreshing of the appreaance coming into the warmer months.

Please feel free to add promotional message. We want to encourage walk by traffic to have anti-wrinkle treatments.

- Poster must not be overly feminine.
- Promote Velarix injections for smoothing and refreshing apprearance (word
velarix can not be used please use 'Anti-wrinkle injection')

Industry/Entity Type

Promotional

Requirements
Must have
• - Logo (attached)

- 4 clinic locations with contact numbers
Suite 305, 48 Farrow Street, Melbourne 9217 4083
587 Bradwell Street, Richmond 9316 7541
Shop 9 Pelling Arcade, Dandenong 9582 6139
17 Drayford Walk, Mount Waverley 9671 3054

- Website
www.lumadorvale.com

- Feel and look of poster to be targeted towards females but not overly feminine, we are a unisex clinic.
Should not have
• - The word velarix can not be used please use 'Anti-wrinkle injection' instead

```html
<!DOCTYPE html>
<html lang="en">
<head>
<meta charset="utf-8">
<title>Spring Anti-Wrinkle Injections</title>
<link href="https://fonts.googleapis.com/css2?family=EB+Garamond:ital,wght@0,400;0,500;0,700;1,700&family=Fira+Sans:wght@200;300&display=swap" rel="stylesheet">
<style>
  :root {
    --paper: #ffffff;
    --ink: #2b2b2b;
    --headline: #ffffff;
    --skin-light: #f6e1d6;
    --skin-mid: #eec3ad;
    --skin-warm: #e7a894;
    --petal-deep: #9e1f45;
    --petal: #d8456f;
    --petal-soft: #ef9ab2;
    --rule: #cfcfcf;
  }
  * { margin: 0; padding: 0; box-sizing: border-box; }
  html, body { width: 847px; height: 1200px; overflow: hidden; background: var(--paper); }
  .poster {
    position: relative;
    width: 847px;
    height: 1200px;
    background: var(--paper);
    color: var(--ink);
    font-family: "EB Garamond", Georgia, serif;
  }
  .brand {
    position: absolute;
    top: 52px;
    left: 0;
    width: 100%;
    text-align: center;
    font-family: "EB Garamond", Georgia, serif;
    font-weight: 500;
    font-size: 22px;
    letter-spacing: 0.5px;
    color: var(--ink);
  }
  .hero {
    position: absolute;
    left: 48px;
    top: 144px;
    width: 748px;
    height: 780px;
    overflow: hidden;
  }
  .hero-photo {
    position: absolute;
    inset: 0;
    background:
      linear-gradient(to bottom, rgba(255,255,255,0) 0%, rgba(255,255,255,0) 62%, var(--paper) 96%),
      radial-gradient(ellipse 55% 45% at 12% 45%, var(--petal-deep) 0%, var(--petal) 45%, rgba(216,69,111,0) 100%),
      radial-gradient(ellipse 70% 60% at 70% 40%, var(--skin-light) 0%, var(--skin-mid) 55%, var(--skin-warm) 100%);
  }
  .headline {
    position: absolute;
    right: 52px;
    top: 150px;
    text-align: right;
    color: var(--headline);
    font-family: "Fira Sans", "Helvetica Neue", Arial, sans-serif;
    text-transform: uppercase;
    line-height: 1.03;
  }
  .headline span { display: block; }
  .headline .season { font-weight: 200; font-size: 74px; letter-spacing: 3px; }
  .headline .treatment { font-weight: 300; font-size: 76px; letter-spacing: 2px; }
  .headline .method { font-weight: 200; font-size: 74px; letter-spacing: 3px; }
  .locations {
    position: absolute;
    top: 946px;
    left: 0;
    width: 100%;
    list-style: none;
    text-align: center;
    font-size: 21px;
    line-height: 30.5px;
    color: var(--ink);
  }
  .locations .phone { font-weight: 700; font-style: italic; margin-left: 4px; }
  .divider {
    position: absolute;
    top: 1102px;
    left: 60px;
    width: 727px;
    border: 0;
    border-top: 1px dashed var(--rule);
  }
  .website {
    position: absolute;
    top: 1128px;
    left: 0;
    width: 100%;
    text-align: center;
    font-weight: 700;
    font-size: 19px;
    letter-spacing: 5px;
    color: var(--ink);
  }
</style>
</head>
<body>
<main class="poster">
  <div class="brand">Lumador Vale Skin Clinic</div>

  <section class="hero">
    <div class="hero-photo" role="img" aria-label="Close-up beauty portrait in profile with pink eyeshadow and closed eyes, beside a bouquet of dried pink and red petals with a cream flower, fading to white at the bottom"></div>
    <h1 class="headline">
      <span class="season">Spring</span>
      <span class="treatment">Anti-Wrinkle</span>
      <span class="method">Injections</span>
    </h1>
  </section>

  <ul class="locations">
    <li>Suite 305, 48 Farrow Street, Melbourne <span class="phone">9217 4083</span></li>
    <li>587 Bradwell Street, Richmond <span class="phone">9316 7541</span></li>
    <li>Shop 9 Pelling Arcade, Dandenong <span class="phone">9582 6139</span></li>
    <li>17 Drayford Walk, Mount Waverley <span class="phone">9671 3054</span></li>
  </ul>

  <hr class="divider">

  <p class="website">www.lumadorvale.com</p>
</main>
</body>
</html>
```